Acai Bowl and Coffee Van need new Menus

We currently have a basic menu that is displayed in an A3 frame. It lacks images, specifically of the Acai Bowls and is difficult to read and understand.

We need a new Acai Bowl Menu and a new Drink Menu but in a more attractive and easier to read format.
We would like images of the Acai Bowls (using Images supplied or make your own) in order to show customers what is on each bowl. Customers chose what granola they would like from the three that are available. Currently we tell customers to check the bottom of the menu as they are often unaware they get to chose.

The drink menu items are simple (we have removed smoothies from our menu entirely).
The drink menu needs to have "Chai Latte" and "Dirty Chai Latte" added as options with the same S,M,L pricing as a Latte.

I have attached images of the menus and a photo of how the menus are displayed on The Moro Cart. Also attached is photos of the Acai Bowls and other food / drink items on the menu if you wish to use them in your design. I have included the files for all of our logo variations.

Our main objective with the menu redesign is to have the menu more appealing and easier to read and understand.

Industry/Entity Type

Food and Coffee

Font styles to use
Other font styles liked:
• Orplid Pro (Fill and Shadow), Trend Sans One

Colors

Designer to choose colors to be used in the design.

Requirements
Must have
• The final design must include prices and be editable in the case of any price changes in the future.

```html
<!DOCTYPE html>
<html lang="en">
<head>
<meta charset="utf-8">
<title>The Moro Cart — Menus</title>
<link href="https://fonts.googleapis.com/css2?family=Josefin+Sans:wght@400;600;700&display=swap" rel="stylesheet">
<style>
  :root{
    --backdrop:#e6e4df;
    --sage:#aab9a9;
    --paper:#ffffff;
    --brown:#7d6a58;
    --ink:#4b4038;
    --mauve:#d8c2c8;
    --mauve-deep:#b9a0a8;
    --white:#ffffff;
  }
  *{box-sizing:border-box;margin:0;padding:0}
  html,body{width:1200px;height:1200px;overflow:hidden}
  body{background:var(--backdrop);font-family:"Josefin Sans",sans-serif;color:var(--ink);position:relative}
  .menu{position:absolute;top:218px;width:540px;height:764px;padding:34px 34px 30px}
  .drinks{left:40px;background:var(--sage)}
  .bowls{left:620px;background:var(--paper)}
  .menu-title{font-weight:700;font-size:60px;line-height:54px;letter-spacing:3px;text-transform:uppercase;
    color:var(--white);-webkit-text-stroke:1.5px var(--brown);text-shadow:4px 4px 0 var(--brown);margin-bottom:28px}
  .bowls .menu-title{color:var(--paper)}

  /* drinks */
  .drink-cols{display:grid;grid-template-columns:1fr 1fr;gap:0 36px}
  .group{margin-bottom:20px}
  .group-head{display:flex;align-items:baseline;font-weight:700;font-size:11px;letter-spacing:1.5px;text-transform:uppercase;margin-bottom:6px}
  .group-head span{flex:1}
  .sizes{display:flex;gap:4px}
  .sizes i{width:30px;text-align:center;font-style:normal;font-size:6px;font-weight:600;letter-spacing:.5px}
  .item{display:flex;align-items:center;font-size:8.5px;font-weight:600;letter-spacing:.6px;text-transform:uppercase;line-height:13px}
  .item .name{flex:1}
  .prices{display:flex;gap:4px}
  .price{width:30px;background:var(--white);text-align:center;font-size:8px;font-weight:700;line-height:11px;margin:1px 0}
  .note{font-size:6.5px;letter-spacing:.4px;text-transform:uppercase;opacity:.8;line-height:9px;margin-bottom:2px}
  .reuse{width:76px;height:76px;border-radius:50%;background:var(--white);display:flex;flex-direction:column;align-items:center;justify-content:center;text-align:center;font-size:7px;font-weight:700;letter-spacing:.5px;text-transform:uppercase;line-height:9px;margin:18px 0 26px 40px}
  .reuse b{font-size:10px}

  /* bowls */
  .step{display:flex;align-items:center;gap:8px;font-weight:700;font-size:11px;letter-spacing:1.2px;text-transform:uppercase;margin-bottom:6px}
  .num{width:20px;height:20px;border-radius:50%;background:var(--brown);color:var(--white);display:flex;align-items:center;justify-content:center;font-size:11px}
  .row-top{display:grid;grid-template-columns:150px 1fr;gap:14px}
  .base-badge{width:96px;height:96px;border-radius:50%;background:var(--mauve);margin:14px 0 0 28px;display:flex;align-items:center;justify-content:center;text-align:center;font-size:6.5px;font-weight:600;text-transform:uppercase;line-height:9px;padding:12px;letter-spacing:.4px}
  .box{background:var(--mauve);padding:10px 12px}
  .granola h4{font-size:8.5px;font-weight:700;letter-spacing:.8px;text-transform:uppercase;margin-bottom:2px}
  .granola p{font-size:6.5px;letter-spacing:.3px;text-transform:uppercase;line-height:8.5px;margin-bottom:8px}
  .granola p:last-child{margin-bottom:0}
  .combos{display:grid;grid-template-columns:1fr 1fr;gap:14px 20px;margin-bottom:16px}
  .bowl-head{display:flex;align-items:center;gap:8px;font-size:9px;font-weight:700;letter-spacing:1px;text-transform:uppercase;margin-bottom:4px}
  .tag{background:var(--mauve-deep);color:var(--white);font-size:7px;padding:2px 6px}
  .bowl-desc{font-size:7.5px;font-weight:700;letter-spacing:.5px;text-transform:uppercase;line-height:10px}
  .bowl-note{font-size:6px;letter-spacing:.3px;text-transform:uppercase;line-height:8px;opacity:.8;margin-top:2px}
  .toppings{display:grid;grid-template-columns:repeat(4,1fr);gap:10px}
  .toppings ul{list-style:none;font-size:7px;font-weight:600;letter-spacing:.5px;text-transform:uppercase;line-height:10px}
  .toppings li::before{content:"• "}
  .topping-price{display:inline-block;margin-top:6px;background:var(--mauve-deep);color:var(--white);font-size:7px;padding:2px 8px}
  .mt{margin-top:16px}
</style>
</head>
<body>

<section class="menu drinks">
  <h1 class="menu-title">Drinks<br>Menu</h1>
  <div class="drink-cols">
    <div>
      <div class="group">
        <div class="group-head"><span>Coffee</span><div class="sizes"><i>SMALL</i><i>REG</i><i>LARGE</i></div></div>
        <div class="item"><span class="name">Cappuccino</span><div class="prices"><b class="price">5.30</b><b class="price">5.50</b><b class="price">7.50</b></div></div>
        <div class="item"><span class="name">Latte</span><div class="prices"><b class="price">5.30</b><b class="price">5.50</b><b class="price">7.50</b></div></div>
        <div class="item"><span class="name">Flat White</span><div class="prices"><b class="price">5.30</b><b class="price">5.50</b><b class="price">7.50</b></div></div>
        <div class="item"><span class="name">Espresso</span><div class="prices"><b class="price">4.00</b><b class="price">5.00</b><b class="price">5.00</b></div></div>
        <div class="item"><span class="name">Long Black</span><div class="prices"><b class="price">4.30</b><b class="price">5.00</b><b class="price">5.50</b></div></div>
        <div class="item"><span class="name">Macchiato</span><div class="prices"><b class="price">5.30</b><b class="price">5.50</b><b class="price">6.00</b></div></div>
      </div>
      <div class="group">
        <div class="group-head"><span>Chocolate</span><div class="sizes"><i>SMALL</i><i>REG</i><i>LARGE</i></div></div>
        <div class="item"><span class="name">Mocha</span><div class="prices"><b class="price">5.50</b><b class="price">6.50</b><b class="price">7.50</b></div></div>
        <div class="item"><span class="name">Hot Chocolate</span><div class="prices"><b class="price">5.00</b><b class="price">6.00</b><b class="price">7.00</b></div></div>
      </div>
      <div class="group">
        <div class="group-head"><span>Chai Latte</span><div class="sizes"><i>SMALL</i><i>REG</i><i>LARGE</i></div></div>
        <div class="item"><span class="name">Chai Latte</span><div class="prices"><b class="price">5.30</b><b class="price">5.50</b><b class="price">7.50</b></div></div>
        <div class="item"><span class="name">Dirty Chai Latte</span><div class="prices"><b class="price">5.80</b><b class="price">6.50</b><b class="price">8.50</b></div></div>
      </div>
      <div class="group">
        <div class="group-head"><span>Cold Beverages</span><div class="sizes"><i>REG</i><i>LARGE</i></div></div>
        <div class="item"><span class="name">Cold Brew Coffee</span><div class="prices"><b class="price">5.50</b><b class="price">6.50</b></div></div>
        <div class="item"><span class="name">Iced Coffee</span><div class="prices"><b class="price">5.50</b><b class="price">7.50</b></div></div>
        <div class="item"><span class="name">Iced Mocha</span><div class="prices"><b class="price">5.50</b><b class="price">7.50</b></div></div>
        <div class="item"><span class="name">Iced Long Black</span><div class="prices"><b class="price">5.00</b><b class="price">6.50</b></div></div>
        <div class="item"><span class="name">Iced Chocolate</span><div class="prices"><b class="price">5.50</b><b class="price">7.50</b></div></div>
        <div class="item"><span class="name">Iced Chai Tea</span><div class="prices"><b class="price">5.00</b><b class="price">6.00</b></div></div>
        <p class="note">Made with ice cream and cream · add a shot of espresso 1.00</p>
      </div>
      <div class="group">
        <div class="group-head"><span>More Beverages</span></div>
        <div class="item"><span class="name">Brewly Kombucha</span><div class="prices"><b class="price">6.50</b></div></div>
        <div class="item"><span class="name">Bottled Water</span><div class="prices"><b class="price">3.00</b></div></div>
      </div>
    </div>
    <div>
      <div class="group">
        <div class="group-head"><span>Extras</span></div>
        <div class="item"><span class="name">Additional Shot</span><div class="prices"><b class="price">0.50</b></div></div>
        <div class="item"><span class="name">Shot of Syrup</span><div class="prices"><b class="price">0.50</b></div></div>
        <p class="note">Vanilla, caramel, hazelnut</p>
      </div>
      <div class="group">
        <div class="group-head"><span>Alternative Milks</span></div>
        <div class="item"><span class="name">Oat Milk</span><div class="prices"><b class="price">+0.70</b></div></div>
        <p class="note">Barista blend, dairy free</p>
        <div class="item"><span class="name">Almond Milk</span><div class="prices"><b class="price">+0.70</b></div></div>
        <p class="note">No sugar</p>
        <div class="item"><span class="name">Soy Milk</span><div class="prices"><b class="price">+0.70</b></div></div>
        <p class="note">Organic, gluten free</p>
        <div class="item"><span class="name">Lactose Free</span><div class="prices"><b class="price">+0.70</b></div></div>
        <p class="note">Full cream</p>
      </div>
      <div class="reuse">Save<br><b>50 cents</b>with your<br>reusable<br>cup</div>
      <div class="group">
        <div class="group-head"><span>Pure Tea</span><div class="sizes"><i>REG</i></div></div>
        <div class="item"><span class="name">English Breakfast</span><div class="prices"><b class="price">4.00</b></div></div>
        <div class="item"><span class="name">Morning Dew</span><div class="prices"><b class="price">4.00</b></div></div>
        <div class="item"><span class="name">Gunpowder Green</span><div class="prices"><b class="price">4.00</b></div></div>
        <div class="item"><span class="name">Chai Tea</span><div class="prices"><b class="price">4.00</b></div></div>
        <div class="item"><span class="name">Peppermint</span><div class="prices"><b class="price">4.00</b></div></div>
        <div class="item"><span class="name">Cacao &amp; Peppermint</span><div class="prices"><b class="price">4.00</b></div></div>
      </div>
    </div>
  </div>
</section>

<section class="menu bowls">
  <h1 class="menu-title">Açai<br>Bowls</h1>

  <div class="row-top">
    <div>
      <div class="step"><span class="num">1</span>Açai Base</div>
      <div class="base-badge">Pure organic açai blended with banana &amp; berries</div>
    </div>
    <div>
      <div class="step"><span class="num">2</span>Pick your ♥ granola</div>
      <div class="box granola">
        <h4>Gingernut Crunch</h4>
        <p>Oats, ginger, golden syrup and toasted coconut, baked until crisp</p>
        <h4>Toasted Almond &amp; Cinnamon</h4>
        <p>Oats, almonds, cinnamon and honey, slow roasted in small batches</p>
        <h4>Cacao, Hazelnut &amp; Chia</h4>
        <p>Oats, cacao, hazelnuts and chia seeds with a touch of maple</p>
      </div>
    </div>
  </div>

  <div class="step mt"><span class="num">3</span>Pick your ♥ topping combo</div>
  <div class="box combos">
    <div>
      <div class="bowl-head">Original Bowl <span class="tag">$15.00</span></div>
      <p class="bowl-desc">Coconut flakes and fresh seasonal fruit</p>
      <p class="bowl-note">A good base, great for kids or simple tastes</p>
    </div>
    <div>
      <div class="bowl-head">Tropical Bowl <span class="tag">$16.50</span></div>
      <p class="bowl-desc">Shredded coconut, passionfruit, mango and pineapple</p>
      <p class="bowl-note">Fresh and light summer favourite</p>
    </div>
    <div>
      <div class="bowl-head">Berry Bowl <span class="tag">$16.50</span></div>
      <p class="bowl-desc">Shredded coconut, goji berries, strawberry and blueberry</p>
      <p class="bowl-note">Packed with antioxidants</p>
    </div>
    <div>
      <div class="bowl-head">Choc Bowl <span class="tag">$17.50</span></div>
      <p class="bowl-desc">Shredded coconut, cacao nibs, banana, strawberry and Hazelda</p>
      <p class="bowl-note">For the chocolate lovers</p>
    </div>
    <div>
      <div class="bowl-head">Crumbco Bowl <span class="tag">$17.50</span></div>
      <p class="bowl-desc">Banana, shredded coconut, goji berries, Crumbco spread and crumble</p>
      <p class="bowl-note">Sweet spiced biscuit goodness</p>
    </div>
    <div>
      <div class="bowl-head">Moro Favourite <span class="tag">$17.50</span></div>
      <p class="bowl-desc">Coconut flakes, goji berries, chia seeds, banana, strawberry and peanut butter</p>
      <p class="bowl-note">Our most loved combo</p>
    </div>
  </div>

  <div class="step"><span class="num">4</span>Additional Toppings</div>
  <div class="box toppings">
    <div><ul><li>Chia seeds</li><li>Passionfruit</li><li>Banana</li><li>Coconut flakes</li><li>Shredded coconut</li></ul><span class="topping-price">$0.50</span></div>
    <div><ul><li>Goji berries</li><li>Cacao nibs</li><li>Honey</li><li>Dates</li><li>Extra fruit</li><li>Extra granola</li></ul><span class="topping-price">$1.00</span></div>
    <div><ul><li>Peanut butter</li><li>Almond butter</li><li>Hazelda</li><li>Crumbco</li></ul><span class="topping-price">$2.00</span></div>
    <div><ul><li>Coastal crunch</li><li>Peanut butter</li><li>Protein slice</li></ul><span class="topping-price">$3.50</span></div>
  </div>
</section>

</body>
</html>
```